Stalwart Noble Alloys Foundries Business Cards

Business Card Design Description
We are wanting to have a new business card designed for our company as we go to a convention. We want to balance business/Modern with elegance and beauty. Our company sells highend jewelry pieces. We want to utilize the colors of Black and Gold and have gold foiled fonts to be physically printed on the business cards.
We also would like to have space to write notes on the back side of the business card. When we meet people at jewelry conventions we would like to write notes if possible.
Here are websites and designs that we like the look and feel of these companies and you can use these as design ideas.
https://www.bellwynne.com
https://www.morvandel.com/en-us/home
Here is our company website link
www.stalwartnaf.com
I also up loaded two versions of our logo.
- Update 4.26.22
I have uploaded photos of a business card we like. this card has raised embossed letters that you can feel. the raise letters are like a plastic but we don't need to use that...I uploaded to show you that we like the experience of the client feeling the characters of the logo. we also would like to have the material as a satin or some material very soft.
- Maybe we can get designs with beautiful gold foiling and raised characters and logos. we like simplicity...not busy but an elegant design. We need to write notes and would like a section where we can write notes. but we want an elegant style and the client has an experience with the feel of the card when they touch the card.
Colors
- Main colors Black & Gold
- white or light colors for small notes section.
Specialty ideals and things we would like to see based on your design styles.
- raised fonts
- raised logos
- gold foiling
- satin/soft finish on the card material.
we are wanting to design a business card that looks elegant and clean. When the client is handed the business card we want them to physically experience the business card as well by touching the raised logos or fonts and the base material is soft satin. I hope this helps with further designs.
thank you all
We uploaded a new contact layout that we have designed in our office. we would like to see how this would look on your designs.
thank you
I just finished uploading the Contact Layout. the colors are just examples. please use this layout as an idea and use colors based on the feed back we have given each of you personally.
Contact Information for Business Card
we need an area to write notes, we would like to have our logos or the diamond of our logo or the business card to have embossed sections to the business card so when the customer touches the card they can feel the logo. we would also like sections of our business card to have gold foiling. we would also like to use a satin soft paper with our card. when the client touches the card its super soft and high quality
Requirements
Must have
- we would like to have our logos or the diamond of our logo or the business card to have embossed sections to the business card so when the customer touches the card they can feel the logo. we would also like sections of our business card to have gold foiling. we would also like to use a satin soft paper with our card. when the client touches the card its super soft and high quality
Nice to have
- we would like to have our logos or the diamond of our logo or the business card to have embossed sections to the business card so when the customer touches the card they can feel the logo. we would also like sections of our business card to have gold foiling.

```html
<!DOCTYPE html>
<html lang="en">
<head>
<meta charset="utf-8">
<title>Stalwart Noble Alloys – Business Card</title>
<link href="https://fonts.googleapis.com/css2?family=Cinzel:wght@400;500&family=Lato:wght@400&display=swap" rel="stylesheet">
<style>
  :root {
    --backdrop: #1b1c1e;
    --card: #2b2c2f;
    --card-edge: #35363a;
    --gold: #c9a227;
    --gold-deep: #a8851c;
    --emboss: #222326;
    --mark: #d9dde2;
  }
  * { margin: 0; padding: 0; box-sizing: border-box; }
  html, body {
    width: 1200px;
    height: 1200px;
    overflow: hidden;
    background: var(--backdrop);
  }
  .card {
    position: absolute;
    left: 100px;
    top: 310px;
    width: 1000px;
    height: 580px;
    background: var(--card);
    border: 1px solid var(--card-edge);
    color: var(--gold);
  }
  .brand {
    position: absolute;
    top: 70px;
    left: 0;
    width: 100%;
    text-align: center;
  }
  .brand-name {
    font-family: "Cinzel", serif;
    font-weight: 500;
    font-size: 50px;
    letter-spacing: 1px;
    color: var(--gold);
    line-height: 1.1;
  }
  .brand-dot {
    display: inline-block;
    width: 22px;
    height: 22px;
    border-radius: 50%;
    background: var(--mark);
    margin-left: 14px;
    vertical-align: 18px;
  }
  .tagline {
    font-family: "Cinzel", serif;
    font-weight: 400;
    font-size: 36px;
    letter-spacing: 1px;
    color: var(--gold);
    margin-top: 6px;
  }
  .embossed-name {
    position: absolute;
    top: 268px;
    left: 0;
    width: 100%;
    text-align: center;
    font-family: "Cinzel", serif;
    font-weight: 500;
    font-size: 44px;
    letter-spacing: 2px;
    color: var(--emboss);
  }
  .contact {
    position: absolute;
    top: 390px;
    left: 230px;
    width: 420px;
    text-align: center;
    font-family: "Lato", sans-serif;
    font-size: 30px;
    line-height: 1.3;
    color: var(--gold);
  }
</style>
</head>
<body>
  <main class="card">
    <header class="brand">
      <div class="brand-name">Stalwart Noble Alloys<span class="brand-dot"></span></div>
      <div class="tagline">– Coins, Jewelry &amp; Diamonds –</div>
    </header>
    <div class="embossed-name">Stalwart Noble Alloys</div>
    <address class="contact" style="font-style: normal;">
      <div class="contact-phone">55501(555)</div>
      <div class="contact-email">infos@stalwartnaf.com</div>
      <div class="contact-web">www.stalwartnaf.com</div>
      <div class="contact-web">www.stalwartnaf.com</div>
    </address>
  </main>
</body>
</html>
```